Business Card Design Project for Female Personal Trainer

I need a business card design to appeal to female clients for my personal training and group fitness boot camp business called 'LumaStride Studio'. It should be girly, fun and have an active/healthy pic or figure incorporated into the business name.

Target Market(s)

- Females 20-65yrs

Industry/Entity Type

Training

Font styles to use
Serif
Sans Serif

Colors
e34197
e567a6

Requirements
Must have
• First Side of Business Card Details :

Odette Calvo
MASTER PERSONAL TRAINER
Cert III & Cert IV in Fitness
Senior First Aid
Mobile: 0493 507 618
Email: lumastride@quellmail.test
Facebook: LumaStride Studio

* Mobile Personal Training *Individual Sessions *Bootcamp *Weight-loss and Toning

Second Side of Business Card I want to offer a free personal consult:
Something like this:

Need direction with your health & fitness goals?

Call now for your free 1 on 1 Personal Training Session with full consultation

Nice to have
• Have a sub-heading for example:

'Promoting healthy living through fitness & nutrition'

- have the colour pink or blue (to appeal to a female)

- a picture/motif//logo attached (sometimes a picture paints a thousand words)

Should not have
• * picture of a person with big muscles or appeal to a man (I'm training women only)

* should not be busy or crammed up look (if I've added to much info above please just use to your discretion).

```html
<!DOCTYPE html>
<html lang="en">
<head>
<meta charset="utf-8">
<title>LumaStride Studio – Business Card</title>
<link rel="stylesheet" href="https://fonts.googleapis.com/css2?family=Oswald:wght@600&family=Roboto:wght@400;500;700&display=swap">
<style>
  :root {
    --backdrop: #e6e7ea;
    --card-white: #ffffff;
    --brand-blue: #0b56a8;
    --ink-grey: #5c5c5c;
    --ink-black: #111111;
    --on-blue: #ffffff;
  }
  * { box-sizing: border-box; margin: 0; padding: 0; }
  html, body {
    width: 1200px; height: 800px; overflow: hidden;
    background: var(--backdrop);
    font-family: "Roboto", Arial, sans-serif;
  }
  .stage {
    position: relative; width: 1200px; height: 800px;
    display: flex; align-items: center; justify-content: center; gap: 40px;
  }
  .card {
    position: relative; width: 540px; height: 309px; overflow: hidden;
    border-radius: 2px;
    box-shadow: 0 2px 6px rgba(0,0,0,.12);
  }

  /* Back side: offer */
  .card--offer {
    background: var(--brand-blue); color: var(--on-blue);
    text-align: center;
  }
  .offer__headline {
    position: absolute; top: 44px; left: 0; right: 0;
    font-family: "Oswald", "Arial Narrow", sans-serif; font-weight: 600;
    font-size: 21px; letter-spacing: .3px; text-transform: uppercase;
  }
  .offer__badge {
    position: absolute; top: 122px; left: 50%; transform: translateX(-50%);
    width: 58px; height: 58px; border-radius: 50%; background: var(--on-blue);
    display: flex; align-items: center; justify-content: center;
  }
  .offer__programs-title {
    position: absolute; top: 196px; left: 0; right: 0;
    font-weight: 700; font-size: 14px;
  }
  .offer__programs {
    position: absolute; top: 220px; left: 0; right: 0;
    font-size: 14px; line-height: 1.35;
  }

  /* Front side: contact */
  .card--contact { background: var(--card-white); }
  .contact__figure {
    position: absolute; left: 130px; bottom: 0; width: 170px; height: 102px;
    background: var(--ink-black);
    border-radius: 40px 70px 0 0;
  }
  .contact__floor {
    position: absolute; left: 0; bottom: 0; width: 300px; height: 20px;
    background: var(--ink-black);
  }
  .contact__name {
    position: absolute; top: 26px; left: 36px;
    font-family: "Oswald", "Arial Narrow", sans-serif; font-weight: 600;
    font-size: 24px; color: var(--brand-blue); text-transform: uppercase; letter-spacing: .3px;
  }
  .contact__credentials {
    position: absolute; top: 64px; left: 36px;
    font-size: 12.5px; line-height: 1.3; color: var(--ink-grey);
    list-style: none;
  }
  .contact__lines {
    position: absolute; top: 132px; left: 36px; list-style: none;
    font-size: 12.5px; line-height: 1.45; color: var(--ink-grey);
  }
  .contact__lines li { display: flex; align-items: center; gap: 8px; }
  .contact__icon { width: 10px; height: 10px; flex: none; }
  .contact__square { width: 9px; height: 9px; background: var(--brand-blue); border-radius: 1px; flex: none; }
  .contact__services {
    position: absolute; right: 30px; top: 118px; list-style: none; text-align: right;
    font-size: 13px; line-height: 1.32; color: var(--ink-grey);
  }
</style>
</head>
<body>
<main class="stage">
  <section class="card card--offer" aria-label="Card back: free consultation offer">
    <h2 class="offer__headline">Need direction with your health &amp; fitness goals?</h2>
    <div class="offer__badge">
      <svg width="34" height="20" viewBox="0 0 34 20" aria-hidden="true">
        <g fill="var(--brand-blue)">
          <rect x="0" y="7" width="3" height="6" rx="1"/>
          <rect x="4" y="3" width="4" height="14" rx="1"/>
          <rect x="8" y="8.5" width="18" height="3"/>
          <rect x="26" y="3" width="4" height="14" rx="1"/>
          <rect x="31" y="7" width="3" height="6" rx="1"/>
        </g>
      </svg>
    </div>
    <p class="offer__programs-title">Fitness Programs</p>
    <p class="offer__programs">Weight loss consults • female specific training<br>body sculpting • HIIT • pre-post natal</p>
  </section>

  <section class="card card--contact" aria-label="Card front: trainer contact details">
    <div class="contact__floor" aria-hidden="true"></div>
    <div class="contact__figure" role="img" aria-label="Black silhouette of a woman lying back with one leg raised in a stretch"></div>
    <h1 class="contact__name">Odette Calvo</h1>
    <ul class="contact__credentials">
      <li>MASTER PERSONAL TRAINER</li>
      <li>Cert III &amp; Cert IV in Fitness</li>
      <li>Senior First Aid</li>
    </ul>
    <ul class="contact__lines">
      <li>
        <svg class="contact__icon" viewBox="0 0 10 10" aria-hidden="true"><rect x="2" y="0" width="6" height="10" rx="1.2" fill="var(--brand-blue)"/><rect x="3" y="1.5" width="4" height="6" fill="#fff"/></svg>
        0493 507 618
      </li>
      <li>
        <svg class="contact__icon" viewBox="0 0 10 10" aria-hidden="true"><rect x="0" y="2" width="10" height="7" fill="var(--brand-blue)"/><path d="M0 2 L5 6 L10 2" stroke="#fff" stroke-width="1" fill="none"/></svg>
        lumastride@quellmail.test
      </li>
      <li>
        <span class="contact__square" aria-hidden="true"></span>
        LumaStride Studio
      </li>
    </ul>
    <ul class="contact__services">
      <li>Mobile Personal Training</li>
      <li>Group Sessions</li>
      <li>Individual Sessions</li>
      <li>Bootcamp</li>
      <li>Boxing for strength and fitness</li>
      <li>Weight-loss and Toning</li>
      <li>General Fitness</li>
    </ul>
  </section>
</main>
</body>
</html>
```